Business Cards for IT Consulting Company (Managed Service Provider)

I am looking to have some business cards printed and would like some designs. We are an IT Consulting company based in Vancouver BC. I would like a nice clean and modern look to the cards. I have uploaded all the versions of my logo so parts can be used as needed. Here is a snippit from our website homepage:

Kelbrook Systems Ltd. is an IT Solutions Partner located in Vancouver BC, Canada. We offer IT solutions and support to customers in the greater Vancouver Area. With expertise in Microsoft platforms, as well as Linux and Mac OSX and over 12 years experience in the IT industry, Kelbrook Systems is dedicated to offering our clients top quality service and products. We take pride in the solutions we offer our customers. The greatest compliment a client can give us is to recommend our services.

Kelbrook Systems Ltd. offers a wide range of IT services from onsite service to remote support and managed service solutions. This allows clients to choose the support path that best suits their company’s needs. Supporting many different sized companies from small to enterprise level over the past 12 years Kelbrook Systems has the experience and expertise needed to ensure things run smoothly. Allowing our clients to focus on doing business.

Revolutionizing the way IT services are delivered.

Kelbrook Systems is dedicated to providing our clients with IT solutions that work and grow with them for years to come. This philosophy helps save money in the long run instead of replacing equipment constantly. Far too often IT solutions are not well thought out and while possibly solving the problem at hand, require replacement due to growth or quality within a very short time frame. Kelbrook Systems takes pride in providing solutions that will last and be able to accommodate growth without the need for replacement.

Industry/Entity Type

Information Technology

Contact Information for Business Card

Kelbrook Systems Ltd.
(Employee Name)
Eml: (Employees Email Address)
Web: kelbrook.me
Ph: 604-555-0142

Font styles to use
Serif
Sans Serif

Requirements
Must have
• The Company logo and company colors.
Nice to have
• - Our tag line: "Revolutionizing IT Services" or "Revolutionizing the way IT services are delivered."
• - Also I really like the idea of nature and technology together blending which is sort of where my logo came from so integrating that somehow onto the business cards would be great.

```html
<!DOCTYPE html>
<html lang="en">
<head>
<meta charset="utf-8">
<title>Kelbrook Systems Ltd. – Business Cards</title>
<link href="https://fonts.googleapis.com/css2?family=Open+Sans:wght@400;600;700&display=swap" rel="stylesheet">
<style>
  :root {
    --brand-blue: #00aeef;
    --brand-grey: #5f6062;
    --band-grey: #636466;
    --paper: #ffffff;
    --backdrop: #e9e9ea;
    --text-light: #ffffff;
  }
  * { margin: 0; padding: 0; box-sizing: border-box; }
  html, body {
    width: 1200px;
    height: 900px;
    overflow: hidden;
    background: var(--backdrop);
    font-family: "Open Sans", Arial, sans-serif;
  }
  .canvas { position: relative; width: 1200px; height: 900px; }

  .card {
    position: absolute;
    background: var(--paper);
    overflow: hidden;
    box-shadow: 0 4px 14px rgba(0,0,0,0.12);
  }

  /* Front card */
  .card-front { left: 77px; top: 34px; width: 589px; height: 364px; }
  .front-brand {
    position: absolute; left: 33px; top: 58px;
    font-size: 33px; font-weight: 600; color: var(--brand-blue);
    letter-spacing: -0.3px; line-height: 1;
  }
  .tagline {
    position: absolute; left: 63px; top: 133px;
    font-size: 17px; font-weight: 600; color: var(--brand-grey);
    letter-spacing: 0.2px;
  }
  .tagline .accent { color: var(--brand-blue); }
  .contact-band {
    position: absolute; left: 0; top: 182px; width: 100%; height: 182px;
    background: var(--brand-blue); color: var(--text-light);
  }
  .person-name {
    position: absolute; left: 31px; top: 26px;
    font-size: 20px; font-weight: 600;
  }
  .contact-list { position: absolute; left: 32px; top: 84px; list-style: none; }
  .contact-list li {
    display: flex; align-items: center; gap: 6px;
    font-size: 15px; height: 24px;
  }
  .contact-list svg { width: 12px; height: 12px; fill: var(--text-light); flex: none; }

  /* Back card */
  .card-back { left: 388px; top: 505px; width: 567px; height: 352px; }
  .back-band {
    position: absolute; left: 0; top: 111px; width: 100%; height: 130px;
    background: var(--band-grey);
    display: flex; align-items: center; justify-content: center;
  }
  .back-brand {
    font-size: 32px; font-weight: 600; color: var(--text-light);
    letter-spacing: -0.3px;
  }
</style>
</head>
<body>
<main class="canvas">
  <section class="card card-front" aria-label="Business card front">
    <div class="front-brand">Kelbrook Systems Ltd.</div>
    <p class="tagline"><span class="accent">REVOLUTIONIZING</span> IT SERVICES</p>
    <div class="contact-band">
      <h1 class="person-name">Daniel Hartley</h1>
      <ul class="contact-list">
        <li>
          <svg viewBox="0 0 24 24" aria-hidden="true"><path d="M6.6 10.8a15.1 15.1 0 0 0 6.6 6.6l2.2-2.2a1 1 0 0 1 1-.25 11.4 11.4 0 0 0 3.6.57 1 1 0 0 1 1 1V20a1 1 0 0 1-1 1A17 17 0 0 1 3 4a1 1 0 0 1 1-1h3.5a1 1 0 0 1 1 1c0 1.25.2 2.45.57 3.57a1 1 0 0 1-.25 1z"/></svg>
          604-555-0142
        </li>
        <li>
          <svg viewBox="0 0 24 24" aria-hidden="true"><path d="M2 5h20v14H2z M3.5 6.5 12 13l8.5-6.5" fill="none" stroke="#fff" stroke-width="2"/><path d="M2 5h20v14H2z"/><path d="M2.5 5.5 12 12.5l9.5-7" fill="none" stroke="#00aeef" stroke-width="1.8"/></svg>
          info@kelbrook.me
        </li>
        <li>
          <svg viewBox="0 0 24 24" aria-hidden="true"><circle cx="12" cy="12" r="10"/><path d="M2 12h20M12 2c3 3 3 17 0 20M12 2c-3 3-3 17 0 20" fill="none" stroke="#00aeef" stroke-width="1.6"/></svg>
          www.kelbrook.me
        </li>
      </ul>
    </div>
  </section>

  <section class="card card-back" aria-label="Business card back">
    <div class="back-band">
      <div class="back-brand">Kelbrook Systems Ltd.</div>
    </div>
  </section>
</main>
</body>
</html>
```